Landcape Construction Company needs a flyer to catch attention

A flyer that can be displayed at several different stores detailing our skills, work produced, experience and contact details. Information can be extracted from our website www.brvkw.co.nz. The flyer should feel very green, with addition of pics of work completed as well as stock images of lush green plants, lawns, landscape or similar. Needs to be eye catching with just enough information to express our experience and commitment to high standards

Target Market(s)

Residential
Landscape Architects

Industry/Entity Type

Landscaping

Font styles to use
Serif

Colors
abd037

Requirements
Must have
• Our logo
Experience
Services offered including pictures
All information avail on our website www.brvkw.co.nz
Nice to have
• stock images of lush greenery like a garden after fresh rainfall
Should not have
• Nothing comes to mind

```html
<!DOCTYPE html>
<html lang="en">
<head>
<meta charset="utf-8">
<title>Greenward Build Company – Flyer</title>
<link rel="stylesheet" href="https://fonts.googleapis.com/css2?family=Lato:wght@400;700&display=swap">
<style>
  :root{
    --page-bg:#ececec;
    --paper:#f2f8dd;
    --green-dark:#127a33;
    --green-mid:#1f8c3a;
    --green-lime:#7dc142;
    --brand-lime:#abd037;
    --ink:#2b3421;
    --white:#ffffff;
  }
  *{margin:0;padding:0;box-sizing:border-box}
  html,body{width:1200px;height:1200px;overflow:hidden;background:var(--page-bg)}
  body{font-family:"Lato",sans-serif;position:relative}
  .flyer{
    position:absolute;left:193px;top:30px;width:934px;height:1310px;
    transform:scale(0.87);transform-origin:top left;
    background:var(--paper);overflow:hidden;
    box-shadow:0 4px 18px rgba(0,0,0,.18);
  }
  .flyer-art{position:absolute;inset:0;width:934px;height:1310px}
  .brand{position:absolute;left:640px;top:30px;width:280px;text-align:center}
  .brand-dot{width:120px;height:120px;border-radius:50%;background:var(--green-mid);margin:0 auto 14px;border:6px solid var(--brand-lime)}
  .brand-name{font-family:"Lato",sans-serif;font-weight:700;color:var(--green-dark);font-size:20px;line-height:22px}
  .intro{
    position:absolute;left:55px;top:486px;width:824px;text-align:center;
    color:var(--white);font-size:16.2px;line-height:20px;
  }
  .services-tab{
    position:absolute;left:253px;top:636px;width:390px;height:98px;
    background:var(--green-lime);border-radius:0 0 20px 20px;
    color:var(--white);font-size:58px;text-align:center;line-height:100px;letter-spacing:1px;
  }
  .services-intro{
    position:absolute;left:30px;top:750px;width:874px;text-align:center;
    color:var(--ink);font-size:15.8px;line-height:20px;
  }
  .service-list{
    position:absolute;top:1016px;width:240px;text-align:center;list-style:none;
    color:var(--ink);font-size:16.5px;line-height:21.4px;text-transform:uppercase;
  }
  .service-list.col-1{left:32px}
  .service-list.col-2{left:340px}
  .service-list.col-3{left:649px}
  .contact{position:absolute;top:1245px;width:260px;text-align:center;color:var(--white);font-size:20px}
  .contact.phone{left:120px}
  .contact.email{left:357px}
  .contact.web{left:592px}
</style>
</head>
<body>
<main class="flyer">
  <svg class="flyer-art" viewBox="0 0 934 1310" xmlns="http://www.w3.org/2000/svg">
    <defs>
      <linearGradient id="grass-fade" x1="0" y1="0" x2="0" y2="1">
        <stop offset="0" stop-color="#f2f8dd" stop-opacity="0"/>
        <stop offset="1" stop-color="#b9dc7c"/>
      </linearGradient>
      <linearGradient id="hero-tone" x1="0" y1="0" x2="1" y2="1">
        <stop offset="0" stop-color="#9a5a3e"/>
        <stop offset=".35" stop-color="#c9c6bd"/>
        <stop offset=".7" stop-color="#5f9a2e"/>
        <stop offset="1" stop-color="#3c3a30"/>
      </linearGradient>
      <linearGradient id="fence-tone" x1="0" y1="0" x2="1" y2="1">
        <stop offset="0" stop-color="#a9693c"/><stop offset="1" stop-color="#4a4540"/>
      </linearGradient>
      <linearGradient id="patio-tone" x1="0" y1="0" x2="0" y2="1">
        <stop offset="0" stop-color="#b9c7cf"/><stop offset=".35" stop-color="#7a8a8a"/><stop offset="1" stop-color="#9a9a92"/>
      </linearGradient>
      <linearGradient id="deck-tone" x1="0" y1="0" x2="0" y2="1">
        <stop offset="0" stop-color="#b7d88a"/><stop offset=".5" stop-color="#e3e6c8"/><stop offset=".55" stop-color="#c88f52"/><stop offset="1" stop-color="#9b6532"/>
      </linearGradient>
      <linearGradient id="lawn-tone" x1="0" y1="0" x2="0" y2="1">
        <stop offset="0" stop-color="#a8a296"/><stop offset=".35" stop-color="#6fa43a"/><stop offset="1" stop-color="#4f8a24"/>
      </linearGradient>
      <linearGradient id="paving-tone" x1="0" y1="0" x2="1" y2="1">
        <stop offset="0" stop-color="#6c6c68"/><stop offset="1" stop-color="#4d4d4a"/>
      </linearGradient>
    </defs>

    <rect class="grass-backdrop" role="img" aria-label="Soft photo of fresh green grass" x="0" y="940" width="934" height="370" fill="url(#grass-fade)"/>

    <path class="hero-photo" role="img" aria-label="Photo of a finished concrete path, lawn and brick seat wall"
          d="M0 0 H375 C470 20 560 90 600 200 L612 300 L600 440 C420 470 200 440 0 375 Z" fill="url(#hero-tone)"/>
    <path class="hero-swoosh" d="M372 0 H470 C560 45 612 130 632 220 L604 216 C575 110 490 25 372 0 Z" fill="var(--green-dark)"/>
    <path d="M470 0 C560 45 612 130 632 220" fill="none" stroke="var(--green-lime)" stroke-width="6"/>

    <path class="intro-band" d="M0 375 C200 440 420 470 600 440 L620 250 C720 250 830 245 934 262 V548 C760 600 620 650 460 652 C300 650 140 600 0 548 Z" fill="var(--green-mid)"/>
    <path d="M0 375 C200 440 420 470 600 440" fill="none" stroke="var(--white)" stroke-width="6"/>

    <g class="work-photo patio">
      <circle cx="656" cy="325" r="108" fill="var(--white)"/>
      <circle role="img" aria-label="Photo of a lakeside paved patio" cx="656" cy="325" r="101" fill="url(#patio-tone)"/>
    </g>
    <g class="work-photo fence">
      <circle cx="509" cy="365" r="106" fill="var(--white)"/>
      <circle role="img" aria-label="Photo of a timber slat fence" cx="509" cy="365" r="99" fill="url(#fence-tone)"/>
    </g>

    <g class="service-photo">
      <circle cx="152" cy="907" r="87" fill="var(--green-dark)"/>
      <circle cx="152" cy="907" r="81" fill="#e8f3c6"/>
      <circle role="img" aria-label="Photo of a timber deck against greenery" cx="152" cy="907" r="76" fill="url(#deck-tone)"/>
    </g>
    <g class="service-photo">
      <circle cx="461" cy="907" r="87" fill="var(--green-dark)"/>
      <circle cx="461" cy="907" r="81" fill="#e8f3c6"/>
      <circle role="img" aria-label="Photo of a lawn with an irrigation sprinkler" cx="461" cy="907" r="76" fill="url(#lawn-tone)"/>
    </g>
    <g class="service-photo">
      <circle cx="769" cy="907" r="87" fill="var(--green-dark)"/>
      <circle cx="769" cy="907" r="81" fill="#e8f3c6"/>
      <circle role="img" aria-label="Photo of square concrete paving" cx="769" cy="907" r="76" fill="url(#paving-tone)"/>
    </g>

    <path d="M0 1290 C120 1195 300 1145 500 1142 C700 1142 850 1158 934 1168" fill="none" stroke="var(--green-lime)" stroke-width="8"/>
    <path class="contact-band" d="M0 1310 V1300 C120 1205 300 1152 500 1150 C700 1150 850 1165 934 1176 V1310 Z" fill="var(--green-mid)"/>

    <g class="contact-icons" fill="none" stroke="var(--green-lime)" stroke-width="3" stroke-linecap="round" stroke-linejoin="round">
      <path d="M243 1212 l6 -2 l5 9 l-4 3 c2 6 6 10 11 13 l3 -4 l9 5 l-2 6 c-12 2 -28 -14 -28 -30 Z" fill="var(--green-lime)" stroke="none"/>
      <rect x="472" y="1217" width="28" height="18" fill="var(--green-lime)" stroke="none"/>
      <polyline points="472,1217 486,1228 500,1217" stroke="var(--green-mid)" stroke-width="2.5"/>
      <circle cx="723" cy="1228" r="11"/>
      <ellipse cx="723" cy="1228" rx="5" ry="11"/>
      <line x1="712" y1="1228" x2="734" y2="1228"/>
    </g>
  </svg>

  <header class="brand">
    <div class="brand-dot"></div>
    <p class="brand-name">The Greenward Build<br>Company Ltd</p>
  </header>

  <p class="intro">With more than 25 years experience in the landscaping industry, The Greenward Build Company offers services to large or small residential and commercial projects. Based in Canterbury, we are locally owned and operated. Whether you have a blank canvas or are looking to rejuvinate your property we are able to advise and make the process easy and stress free. From paving, pergolas and decks to concrete or planting your dream garden we have the expertise to help.</p>

  <h2 class="services-tab">SERVICES</h2>

  <p class="services-intro">As a full construction landscaping company, we formally offer the following services. However, we regularly work with clients who want something a little out of the box. If there is something in particular you are after, we are happy to discuss options with you.</p>

  <ul class="service-list col-1"><li>Patios</li><li>Paving</li><li>Concrete</li><li>Water Features</li><li>Decking</li></ul>
  <ul class="service-list col-2"><li>Fencing</li><li>Boardwalks</li><li>Timber</li><li>Planter Boxes</li><li>Pergolas</li></ul>
  <ul class="service-list col-3"><li>Retaining Walls</li><li>Gardens &amp; Lawns</li><li>Irrigation</li><li>Project<br>Management</li><li>Consultation</li></ul>

  <p class="contact phone">021 480 527</p>
  <p class="contact email">mark@brvkw.co.nz</p>
  <p class="contact web">www.brvkw.co.nz</p>
</main>
</body>
</html>
```